Solo improvising pianist/composer needs album cover art for contemporary new-age recording

My music is completely improvised on the piano (or keyboard), meaning the context of the production is spontaneous. Thus I need an artist who works in a through-composed, non-conventional design method. My sound is a hybrid of Neo-Classicism, Impressionism, Jazz, Modern Jazz, and 20th Century composed music - for e.g., composers ranging from Lucien Tabard to Oleg Kuznetsov, Peter Wilcox to Grant Tolliver. I would prefer a more classical approach to the art design, as in using Impressionistic painting techniques, like Durel, to match some of my Tabard-inspired improvisations. Also, try to include some Surrealistic symbols, mixed with some imagery from the solar system, as in planets, or perhaps vague references to an alien planet. Please don't get hyper digital with that though. I'm looking more for a contemporary piece of art design, in that it looks like a sculpture, a painting or an installation. For example, maybe it could be a setting in an art gallery with a piano melting into a planet, with some jungle brush in the background, etc, etc. It also needs to show the musical, piano improvisation element in the design, in case I don't put my name or the album title on the front.

Target Market(s)

Sophisticated jazz, modern jazz and contemporary New-Age listeners. Elitist folks who want more eclectic, avant-garde music that is definitely outside the mainstream, but contains traditional aspects of improvised music, such as bebop and Latin jazz.

Industry/Entity Type

Performing Art

Font styles to use
Sans Serif

Colors

Designer to choose colors to be used in the design.

Requirements
Must have
• It must have, as I stated above in the project description, some element of Impressionism - Durel, Ter Huizen, etc.. French style, since I have French sounding improvised music in the style of Tabard. I want some Surrealistic imagery, like Lebrusse, and maybe some exotic organic symbolism. It must have some sort of musical improvisation idea, some reference to a piano, or hands, or something that exudes esoteric musical phenomena.
Nice to have
• It would be nice to have some sort of astronomical reference to another planet, or galaxy, so some sort of sci-fi aspect, just a touch.
Should not have
• I don't want it too dark, or too happy, somewhere in between. And not too busy, keep it original, but refined. Also, I don't want it looking like it was done digitally. I want it to look more in the classical, contemporary art world, as in Expressionistic. It should look like a painting, not a hyper digital sci-fi Wallpaper background.

```html
<!DOCTYPE html>
<html lang="en">
<head>
<meta charset="utf-8">
<title>Improvised New-Age Piano – Now Playing</title>
<link href="https://fonts.googleapis.com/css2?family=Montserrat:wght@400;500;600&display=swap" rel="stylesheet">
<style>
  :root {
    --backdrop: #c9cbc6;
    --screen-top: #4f4339;
    --screen-bottom: #272322;
    --text-main: #ffffff;
    --text-muted: #b9b1aa;
    --text-faint: #9b928b;
    --accent: #1f8a55;
    --track: #5d5650;
    --badge-bg: #3d3633;
    --art-main: #e4e2e6;
    --art-tone: #c9b7d6;
  }
  * { margin: 0; padding: 0; box-sizing: border-box; }
  html, body { width: 1200px; height: 900px; overflow: hidden; }
  body {
    background: var(--backdrop);
    font-family: "Montserrat", sans-serif;
    position: relative;
  }
  .player-screen {
    position: absolute;
    left: 456px; top: 116px;
    width: 288px; height: 580px;
    border-radius: 38px;
    background: linear-gradient(180deg, var(--screen-top) 0%, #3f3631 50%, var(--screen-bottom) 100%);
    overflow: hidden;
    color: var(--text-main);
  }
  .status-bar {
    position: absolute; top: 6px; left: 24px; right: 22px;
    display: flex; justify-content: space-between; align-items: center;
    font-size: 9px; font-weight: 600;
  }
  .status-icons { display: flex; gap: 4px; align-items: center; }
  .header { position: absolute; top: 32px; left: 0; right: 0; text-align: center; }
  .header-label { font-size: 7px; letter-spacing: 0.3px; color: var(--text-faint); }
  .header-title { font-size: 9px; font-weight: 600; margin-top: 5px; }
  .header-back { position: absolute; left: 24px; top: 40px; }
  .header-menu { position: absolute; right: 32px; top: 38px; }
  .cover-art {
    position: absolute; left: 24px; top: 117px;
    width: 231px; height: 230px; border-radius: 30px;
    background: radial-gradient(circle at 50% 45%, var(--art-tone) 0%, #d7cfe0 30%, var(--art-main) 65%, #eceaee 100%);
  }
  .track-info { position: absolute; top: 417px; left: 0; right: 0; text-align: center; }
  .track-title { font-size: 10.5px; font-weight: 500; }
  .track-artist { font-size: 8.5px; color: var(--text-muted); margin-top: 4px; }
  .progress { position: absolute; top: 460px; left: 24px; width: 232px; height: 2px; background: var(--track); }
  .progress-fill { width: 88px; height: 2px; background: var(--accent); }
  .progress-knob {
    position: absolute; left: 81px; top: -6px;
    width: 14px; height: 14px; border-radius: 50%; background: var(--text-main);
  }
  .controls { position: absolute; top: 477px; left: 0; right: 0; height: 44px; }
  .controls svg { position: absolute; }
  .play-button {
    position: absolute; left: 118px; top: 0;
    width: 44px; height: 44px; border-radius: 50%; background: var(--text-main);
  }
  .footer-row { position: absolute; top: 531px; left: 0; right: 0; height: 14px; }
  .footer-row svg { position: absolute; }
  .quality-badge {
    position: absolute; left: 124px; top: 1px;
    padding: 2px 6px; border-radius: 4px;
    background: var(--badge-bg); font-size: 6.5px; font-weight: 500; color: var(--text-muted);
  }
  .home-indicator {
    position: absolute; left: 92px; top: 561px;
    width: 96px; height: 3px; border-radius: 2px; background: #d9d4d0;
  }
</style>
</head>
<body>
  <main class="player-screen">
    <div class="status-bar">
      <span class="status-time">9:24</span>
      <span class="status-icons">
        <svg width="11" height="7" viewBox="0 0 11 7"><rect x="0" y="5" width="2" height="2" fill="#fff"/><rect x="3" y="3.5" width="2" height="3.5" fill="#fff"/><rect x="6" y="2" width="2" height="5" fill="#fff"/><rect x="9" y="0" width="2" height="7" fill="#fff"/></svg>
        <svg width="10" height="7" viewBox="0 0 10 7"><path d="M0 2.5 Q5 -1.5 10 2.5 L8.6 3.8 Q5 1 1.4 3.8Z M2.6 5 Q5 3 7.4 5 L5 7Z" fill="#fff"/></svg>
        <svg width="12" height="6" viewBox="0 0 12 6"><rect width="12" height="6" rx="1.5" fill="#fff"/></svg>
      </span>
    </div>

    <svg class="header-back" width="16" height="9" viewBox="0 0 16 9"><path d="M1 1 L8 8 L15 1" stroke="#c8c0ba" stroke-width="1.4" fill="none"/></svg>
    <header class="header">
      <p class="header-label">PLAYING FROM PLAYLIST</p>
      <p class="header-title">Improvised New-Age Piano</p>
    </header>
    <svg class="header-menu" width="4" height="14" viewBox="0 0 4 14"><circle cx="2" cy="2" r="1.4" fill="#c8c0ba"/><circle cx="2" cy="7" r="1.4" fill="#c8c0ba"/><circle cx="2" cy="12" r="1.4" fill="#c8c0ba"/></svg>

    <div class="cover-art" role="img" aria-label="Album cover: watercolour painting of piano keys in violet, yellow and pale green, melting downward on a white ground"></div>

    <section class="track-info">
      <h1 class="track-title">The Art of Contemporary Improvisation</h1>
      <p class="track-artist">Corwin Ashby</p>
    </section>

    <div class="progress"><div class="progress-fill"></div><div class="progress-knob"></div></div>

    <nav class="controls">
      <svg style="left:23px;top:16px" width="14" height="12" viewBox="0 0 14 12"><path d="M7 11.5 L1.2 5.6 A3.2 3.2 0 0 1 7 2 A3.2 3.2 0 0 1 12.8 5.6Z" fill="#c8c0ba"/></svg>
      <svg style="left:77px;top:15px" width="14" height="14" viewBox="0 0 14 14"><rect x="0" y="0" width="2.4" height="14" fill="#fff"/><path d="M14 0 L3 7 L14 14Z" fill="#fff"/></svg>
      <div class="play-button"><svg style="left:16px;top:13px" width="14" height="18" viewBox="0 0 14 18"><path d="M0 0 L14 9 L0 18Z" fill="#2a2523"/></svg></div>
      <svg style="left:188px;top:15px" width="14" height="14" viewBox="0 0 14 14"><path d="M0 0 L11 7 L0 14Z" fill="#fff"/><rect x="11.6" y="0" width="2.4" height="14" fill="#fff"/></svg>
      <svg style="left:241px;top:15px" width="15" height="15" viewBox="0 0 15 15"><circle cx="7.5" cy="7.5" r="6.6" stroke="#c8c0ba" stroke-width="1.1" fill="none"/><rect x="4" y="7" width="7" height="1.2" fill="#c8c0ba"/></svg>
    </nav>

    <div class="footer-row">
      <svg style="left:25px;top:2px" width="13" height="10" viewBox="0 0 13 10"><path d="M2 4 V2.5 H10.5 M9 1 L10.8 2.5 L9 4 M11 6 V7.5 H2.5 M4 6 L2.2 7.5 L4 9" stroke="#c8c0ba" stroke-width="1.1" fill="none"/></svg>
      <span class="quality-badge">HI-FI</span>
      <svg style="left:242px;top:2px" width="12" height="10" viewBox="0 0 12 10"><path d="M0 2 H3 L8 8 H11 M0 8 H3 L8 2 H11 M9.5 0.5 L11.2 2 L9.5 3.5 M9.5 6.5 L11.2 8 L9.5 9.5" stroke="#c8c0ba" stroke-width="1" fill="none"/></svg>
    </div>

    <div class="home-indicator"></div>
  </main>
</body>
</html>
```